professional business card design for technology company

We are a small technology consulting firm, specialising in consulting based around Cloud and Managed services. Our colour scheme is yellow, blue and white, as you can see in the logos. Although we are based in melbourne australia, due to the nature of our work, our clients can be located anywhere. We are looking for a clean, professional, positive look - similar to our company logo

Target Market(s)

small business

Industry/Entity Type

Business

Contact Information for Business Card

eye catching, designed to incorporate some level of raised printing. Must contain website address, phone number, name and job title

Requirements
Must have
• Logo (attached) - use of the same colour scheme

```html
<!DOCTYPE html>
<html lang="en">
<head>
<meta charset="utf-8">
<title>Nuvora Business Card</title>
<link href="https://fonts.googleapis.com/css2?family=Open+Sans:wght@400;600;700&display=swap" rel="stylesheet">
<style>
  :root {
    --bg: #2b2826;
    --card: #141414;
    --card-edge: #1d1d1d;
    --divider: #2e2e2e;
    --yellow: #f3d11a;
    --blue: #5bc2ea;
    --white: #f2f2f2;
  }
  * { margin: 0; padding: 0; box-sizing: border-box; }
  html, body {
    width: 1200px; height: 844px; overflow: hidden;
    background: var(--bg);
    font-family: "Open Sans", Arial, sans-serif;
  }
  .canvas {
    position: relative; width: 1200px; height: 844px;
    display: flex; align-items: center; justify-content: center; gap: 60px;
  }
  .card {
    width: 500px; height: 290px;
    background: var(--card);
    border: 1px solid var(--card-edge);
    border-radius: 3px;
    box-shadow: 0 14px 30px rgba(0,0,0,.45);
    position: relative;
  }
  /* Front */
  .card-front { display: flex; }
  .front-brand {
    width: 44%; display: flex; align-items: center; justify-content: center; gap: 10px;
    border-right: 1px solid var(--divider);
    margin: 40px 0;
  }
  .brand-dot { width: 14px; height: 14px; border-radius: 50%; background: var(--blue); }
  .brand-name { font-weight: 700; font-size: 26px; color: var(--blue); letter-spacing: .5px; }
  .front-details {
    flex: 1; padding: 58px 0 0 30px; color: var(--yellow); font-size: 13.5px; line-height: 1.4;
  }
  .person-name { font-weight: 600; font-size: 20px; line-height: 1.2; }
  .person-title { color: var(--blue); margin-bottom: 12px; }
  .address { margin-bottom: 18px; }
  .contact-line .value { color: var(--blue); }
  /* Back */
  .card-back { display: flex; align-items: center; justify-content: center; gap: 14px; }
  .card-back .brand-dot { width: 22px; height: 22px; }
  .card-back .brand-name { color: var(--white); font-size: 44px; }
</style>
</head>
<body>
<main class="canvas">
  <section class="card card-front">
    <div class="front-brand">
      <span class="brand-dot"></span>
      <span class="brand-name">Nuvora</span>
    </div>
    <div class="front-details">
      <p class="person-name">Sam Carter</p>
      <p class="person-title">Managing Director</p>
      <p class="address">12345, Address Goes Here<br>Country Name, 123456.</p>
      <p class="contact-line">T: <span class="value">044-987 654 321</span></p>
      <p class="contact-line">E: <span class="value">hello@nuvora.com</span></p>
      <p class="contact-line">W: <span class="value">www.nuvora.com</span></p>
    </div>
  </section>
  <section class="card card-back">
    <span class="brand-dot"></span>
    <span class="brand-name">Nuvora</span>
  </section>
</main>
</body>
</html>
```